Fernwick Digital Marketing Agency Website Design. I need a new website for my digital marketing agency. It needs to be FAST and easy to use. I want to be able to add videos to the main homepage like this page: https://www.lumatreeweb.example/search-marketing/cleveland-ohio-seo-companyI'd like to have the request quote tab on the top right side as well as my number above it. The following website is my favorite overall: http://www.vantorelgroup.example/ I'd love to copy something like that.

***** Website I want to copy: http://www.vantorelgroup.example/services/ ******
Updates

This needs to be a Wordpress website. Sorry for any confusion as this is the first time using MakerQuill. I need the homepage as described as well as a Services Page and Contact Us page. Services page should be simply yet creative with a spot for me to insert up to 8 services.

Target Market(s)

Business owners

Industry/Entity Type

Digital Marketing

Coding

Coded - Design and coding required

Number of Pages Required

3 page

Font styles to use
Other font styles liked:
• Oswald

Colors

Designer to choose colors to be used in the design.

Requirements
Must have
• I need to have a nice design/template to work off of in Wordpress. It needs to be bright and vibrant yet elegant in design.
Nice to have
• CTA at the top right as well as a place for the phone number. http://www.vantorelgroup.example/services/

```html
<!DOCTYPE html>
<html lang="en">
<head>
<meta charset="utf-8">
<title>Fernwick Digital Marketing Agency</title>
<link href="https://fonts.googleapis.com/css2?family=Roboto+Slab:wght@300;400&family=Source+Sans+3:wght@400;600;700&family=Montserrat:wght@700&display=swap" rel="stylesheet">
<style>
  :root {
    --white: #ffffff;
    --panel: #f7f7f7;
    --ink: #333333;
    --muted: #7a7a7a;
    --orange: #f0aa4c;
    --brown: #8c6a38;
    --dark: #1b1b1d;
    --footer: #0c0c0d;
    --footer-link: #b9b9b9;
  }
  * { box-sizing: border-box; margin: 0; padding: 0; }
  html, body { width: 1200px; height: 2812px; overflow: hidden; background: var(--white); }
  body { position: relative; font-family: "Source Sans 3", Arial, sans-serif; color: var(--ink); }

  .services { position: absolute; left: 0; top: 0; width: 1200px; height: 724px; background: var(--white); }
  .service { position: absolute; height: 334px; display: flex; }
  .service-media { height: 100%; }
  .service-body { height: 100%; background: var(--panel); padding: 30px 24px 0 24px; }
  .service-title { font-family: "Roboto Slab", Georgia, serif; font-weight: 400; font-size: 18px; letter-spacing: .5px; color: #333; text-transform: uppercase; margin-bottom: 14px; }
  .service-text { font-size: 14px; line-height: 25px; color: var(--muted); }
  .btn { display: inline-block; background: var(--orange); color: var(--white); border-radius: 20px; font-weight: 600; font-size: 13px; text-align: center; text-decoration: none; }
  .service .btn { position: absolute; bottom: 30px; width: 120px; height: 40px; line-height: 40px; }

  .team { position: absolute; left: 0; top: 724px; width: 1200px; height: 1282px; background: var(--brown); color: var(--white); }
  .team-title { position: absolute; top: 76px; width: 100%; text-align: center; font-family: "Roboto Slab", Georgia, serif; font-weight: 300; font-size: 34px; letter-spacing: .5px; }
  .member { position: absolute; width: 290px; text-align: center; }
  .member-photo { width: 258px; height: 294px; margin: 0 auto; }
  .member-role { margin-top: 24px; font-size: 10px; font-weight: 700; }
  .member-name { margin-top: 8px; font-family: "Roboto Slab", Georgia, serif; font-size: 18px; font-weight: 400; }
  .member-bio { margin-top: 12px; font-size: 13px; line-height: 24px; font-weight: 700; color: #fdf3d8; }

  .subscribe { position: absolute; left: 0; top: 2026px; width: 1200px; height: 500px;
    background: radial-gradient(circle at 1060px 140px, #3a2a26 0, transparent 200px), linear-gradient(160deg, #2a2a2c 0%, #1c1c1e 50%, #141416 100%); color: var(--white); }
  .subscribe-title { position: absolute; left: 132px; top: 64px; font-family: "Roboto Slab", Georgia, serif; font-weight: 400; font-size: 32px; }
  .subscribe-lede { position: absolute; left: 132px; top: 118px; width: 900px; font-family: "Roboto Slab", Georgia, serif; font-size: 24px; line-height: 28px; }
  .field { position: absolute; left: 382px; width: 438px; height: 52px; background: var(--white); border-radius: 3px; padding-left: 20px; line-height: 52px; font-size: 12px; color: #8a8a8a; }
  .subscribe .btn { position: absolute; left: 382px; top: 350px; width: 218px; height: 42px; line-height: 42px; font-size: 15px; }

  .footer { position: absolute; left: 0; top: 2526px; width: 1200px; height: 286px; background: var(--footer); color: var(--white); }
  .footer-col { position: absolute; top: 104px; }
  .footer-heading { font-family: "Montserrat", Arial, sans-serif; font-weight: 700; font-size: 11px; letter-spacing: 1.5px; text-transform: uppercase; line-height: 14px; margin-bottom: 12px; }
  .footer-about { width: 260px; font-size: 13px; line-height: 24px; font-weight: 600; }
  .footer-links { list-style: none; }
  .footer-links li { font-size: 13px; line-height: 25px; color: var(--footer-link); }
</style>
</head>
<body>

<section class="services">
  <article class="service" style="left:24px; top:10px;">
    <div class="service-media" role="img" aria-label="Illustration of analytics dashboards on a monitor and tablet" style="width:280px; background:linear-gradient(135deg,#e8f3f7,#cfe6ec);"></div>
    <div class="service-body" style="width:280px;">
      <h3 class="service-title">Lead Generation</h3>
      <p class="service-text">Dignissimos asperiores vitae velit veniam totam fuga molestias accusamus alias autem provident. Odit ab aliquam dolor eius molestias accusamus alias autem provident. Odit ab aliquam dolor eius.</p>
      <a class="btn" href="#">Learn more</a>
    </div>
  </article>
  <article class="service" style="left:600px; top:10px;">
    <div class="service-media" role="img" aria-label="Illustration of a globe with a rocket" style="width:294px; background:linear-gradient(135deg,#ffffff,#bfe9ef);"></div>
    <div class="service-body" style="width:282px;">
      <h3 class="service-title">Web Development</h3>
      <p class="service-text">Dignissimos asperiores vitae velit veniam totam fuga molestias accusamus alias autem provident. Odit ab aliquam dolor eius molestias accusamus alias autem provident. Odit ab aliquam dolor eius.</p>
      <a class="btn" href="#">Learn more</a>
    </div>
  </article>
  <article class="service" style="left:24px; top:374px;">
    <div class="service-media" role="img" aria-label="Photo of colourful social app cubes" style="width:280px; background:linear-gradient(135deg,#3c5fa8,#c7304e 50%,#e9b83a);"></div>
    <div class="service-body" style="width:280px;">
      <h3 class="service-title">Social Media</h3>
      <p class="service-text">Dignissimos asperiores vitae velit veniam totam fuga molestias accusamus alias autem provident. Odit ab aliquam dolor eius molestias accusamus alias autem provident. Odit ab aliquam dolor eius.</p>
      <a class="btn" href="#">Learn more</a>
    </div>
  </article>
  <article class="service" style="left:600px; top:374px;">
    <div class="service-media" role="img" aria-label="Illustration of a web page with coins and a clicking hand" style="width:294px; background:linear-gradient(135deg,#e6f3f6,#f7c26a);"></div>
    <div class="service-body" style="width:282px;">
      <h3 class="service-title">PPC Campaigns</h3>
      <p class="service-text">Dignissimos asperiores vitae velit veniam totam fuga molestias accusamus alias autem provident. Odit ab aliquam dolor eius molestias accusamus alias autem provident. Odit ab aliquam dolor eius.</p>
      <a class="btn" href="#">Learn more</a>
    </div>
  </article>
</section>

<section class="team">
  <h2 class="team-title">MEET OUR TEAM</h2>

  <div class="member" style="left:23px; top:164px;"><div class="member-photo" role="img" aria-label="Team member portrait" style="background:linear-gradient(160deg,#566068,#2f3236);"></div><p class="member-role">Sr. SEO Strategist</p><h4 class="member-name">Dale Porter</h4><p class="member-bio">Nullam ac urna eu felis dapibus condimentum sit amet a augue. Sed non neque elit. Sed ut imperdiet nisi.</p></div>
  <div class="member" style="left:313px; top:164px;"><div class="member-photo" role="img" aria-label="Team member seated by a window" style="background:linear-gradient(160deg,#d8d4c8,#4a4c52);"></div><p class="member-role">Sr. SEO Strategist</p><h4 class="member-name">Dale Porter</h4><p class="member-bio">Nullam ac urna eu felis dapibus condimentum sit amet a augue. Sed non neque elit. Sed ut imperdiet nisi.</p></div>
  <div class="member" style="left:601px; top:164px;"><div class="member-photo" role="img" aria-label="Team member portrait" style="background:linear-gradient(160deg,#566068,#2f3236);"></div><p class="member-role">Sr. SEO Strategist</p><h4 class="member-name">Dale Porter</h4><p class="member-bio">Nullam ac urna eu felis dapibus condimentum sit amet a augue. Sed non neque elit. Sed ut imperdiet nisi.</p></div>
  <div class="member" style="left:889px; top:164px;"><div class="member-photo" role="img" aria-label="Team member at a desk with a phone" style="background:linear-gradient(160deg,#1f4a4c,#2a2624);"></div><p class="member-role">Sr. SEO Strategist</p><h4 class="member-name">Dale Porter</h4><p class="member-bio">Nullam ac urna eu felis dapibus condimentum sit amet a augue. Sed non neque elit. Sed ut imperdiet nisi.</p></div>

  <div class="member" style="left:23px; top:690px;"><div class="member-photo" role="img" aria-label="Team member at a desk with a phone" style="background:linear-gradient(160deg,#1f4a4c,#2a2624);"></div><p class="member-role">Sr. SEO Strategist</p><h4 class="member-name">Dale Porter</h4><p class="member-bio">Nullam ac urna eu felis dapibus condimentum sit amet a augue. Sed non neque elit. Sed ut imperdiet nisi.</p></div>
  <div class="member" style="left:313px; top:690px;"><div class="member-photo" role="img" aria-label="Team member seated by a window" style="background:linear-gradient(160deg,#d8d4c8,#4a4c52);"></div><p class="member-role">Sr. SEO Strategist</p><h4 class="member-name">Dale Porter</h4><p class="member-bio">Nullam ac urna eu felis dapibus condimentum sit amet a augue. Sed non neque elit. Sed ut imperdiet nisi.</p></div>
  <div class="member" style="left:601px; top:690px;"><div class="member-photo" role="img" aria-label="Team member portrait" style="background:linear-gradient(160deg,#566068,#2f3236);"></div><p class="member-role">Sr. SEO Strategist</p><h4 class="member-name">Dale Porter</h4><p class="member-bio">Nullam ac urna eu felis dapibus condimentum sit amet a augue. Sed non neque elit. Sed ut imperdiet nisi.</p></div>
  <div class="member" style="left:889px; top:690px;"><div class="member-photo" role="img" aria-label="Team member at a desk with a phone" style="background:linear-gradient(160deg,#1f4a4c,#2a2624);"></div><p class="member-role">Sr. SEO Strategist</p><h4 class="member-name">Dale Porter</h4><p class="member-bio">Nullam ac urna eu felis dapibus condimentum sit amet a augue. Sed non neque elit. Sed ut imperdiet nisi.</p></div>
</section>

<section class="subscribe" role="img" aria-label="Dark background photo of a laptop keyboard and charts">
  <h2 class="subscribe-title">Subscribe to Happy Hour!</h2>
  <p class="subscribe-lede">Subscribe to our newsletter to ensure that your company website is pulling in traffic, learn about our staff, and to get random facts each month!</p>
  <div class="field" style="top:194px;">Email</div>
  <div class="field" style="top:272px;">Company Name</div>
  <a class="btn" href="#">Sign Up!</a>
</section>

<footer class="footer">
  <div class="footer-col" style="left:36px; top:104px;">
    <h5 class="footer-heading" style="width:240px;">About Fernwick Digital Marketing Company</h5>
    <p class="footer-about">Facilis ipsum reprehenderit nemo molestias. Aut cum mollitia reprehenderit. Eos cumque dicta adipisci architecto culpa amet.</p>
  </div>
  <div class="footer-col" style="left:422px;">
    <h5 class="footer-heading">Learning</h5>
    <ul class="footer-links"><li>Course</li><li>Blog</li><li>Contact</li><li>Terms</li><li>Meetups</li></ul>
  </div>
  <div class="footer-col" style="left:616px;">
    <h5 class="footer-heading">Learn &amp; Grow</h5>
    <ul class="footer-links"><li>Blog</li><li>Privacy</li><li>Testimonials</li><li>Handbook</li><li>Held Desk</li></ul>
  </div>
  <div class="footer-col" style="left:810px;">
    <h5 class="footer-heading">Engage Us</h5>
    <ul class="footer-links"><li>Marketing</li><li>Visual Assistant</li><li>System Analysis</li><li>Advertise</li></ul>
  </div>
  <div class="footer-col" style="left:1004px;">
    <h5 class="footer-heading">Legal</h5>
    <ul class="footer-links"><li>Find Designers</li><li>Find Developers</li><li>Teams</li><li>Advertise</li><li>API</li></ul>
  </div>
</footer>

</body>
</html>
```